Letterhead Design

I would like 2 different letterheads. One with each logo I have attached. Business info:
Larkfield Medical Billing, LLC
3870 N Cedar
Ossing, KS 66492
(866) 555-0143

```html
<!DOCTYPE html>
<html lang="en">
<head>
<meta charset="utf-8">
<title>Larkfield Medical Billing — Letterhead</title>
<link rel="stylesheet" href="https://fonts.googleapis.com/css2?family=Questrial&display=swap">
<style>
  :root {
    --backdrop: #e9ebec;
    --paper: #ffffff;
    --brand-deep: #0d5674;
    --brand-mid: #1a7591;
    --brand-light: #9cc3d4;
    --ink: #2a2a2a;
  }
  * { box-sizing: border-box; margin: 0; padding: 0; }
  html, body {
    width: 1200px;
    height: 1000px;
    overflow: hidden;
    background: var(--backdrop);
    font-family: "Questrial", sans-serif;
  }
  .letterhead {
    position: absolute;
    left: 237px;
    top: 30px;
    width: 726px;
    height: 940px;
    background: var(--paper);
    box-shadow: 0 2px 10px rgba(0,0,0,0.12);
  }
  .brand {
    position: absolute;
    left: 40px;
    top: 40px;
    display: flex;
    align-items: center;
    gap: 10px;
    color: var(--brand-deep);
    font-size: 17px;
    letter-spacing: 0.5px;
  }
  .brand-mark {
    width: 26px;
    height: 26px;
    background: var(--brand-deep);
  }
  .contact {
    position: absolute;
    left: 524px;
    top: 36px;
    font-size: 12.5px;
    line-height: 16px;
    color: var(--ink);
  }
  .contact-phone {
    display: flex;
    align-items: center;
    gap: 7px;
    font-size: 13px;
  }
  .contact-phone svg { width: 11px; height: 11px; }
  .footer-emblem {
    position: absolute;
    left: 328px;
    top: 853px;
    width: 70px;
    height: 62px;
    background: linear-gradient(180deg, #3c86a6 0%, #7aa8bd 100%);
    opacity: 0.55;
    border-radius: 4px;
  }
  .footer-rule {
    position: absolute;
    left: 0;
    top: 906px;
    width: 726px;
    height: 34px;
  }
</style>
</head>
<body>
  <main class="letterhead">
    <header>
      <div class="brand">
        <span class="brand-mark"></span>
        <span class="brand-name">Larkfield Medical Billing, LLC</span>
      </div>
      <address class="contact" style="font-style: normal;">
        <div class="contact-phone">
          <svg viewBox="0 0 12 12" aria-hidden="true">
            <rect width="12" height="12" rx="1.5" fill="#1a7591"/>
            <path d="M4 2.5 L5.3 4.2 L4.6 5 Q5.5 6.8 7 7.4 L7.8 6.7 L9.5 8 L8.8 9.5 Q4.5 9.3 2.6 3.2 Z" fill="#fff"/>
          </svg>
          <span>(866) 555-0143</span>
        </div>
        <div>Larkfield Medical Billing, LLC,</div>
        <div>3870 N Cedar, Ossing, KS 66492</div>
      </address>
    </header>

    <div class="footer-emblem" role="img" aria-label="Crossed wheat stalks emblem"></div>

    <svg class="footer-rule" viewBox="0 0 726 34" preserveAspectRatio="none" aria-hidden="true">
      <defs>
        <linearGradient id="bandGradient" x1="0" x2="1" y1="0" y2="0">
          <stop offset="0" stop-color="#9cc3d4"/>
          <stop offset="0.55" stop-color="#1a7591"/>
          <stop offset="1" stop-color="#0d5674"/>
        </linearGradient>
        <linearGradient id="swooshGradient" x1="0" x2="1" y1="0" y2="0">
          <stop offset="0" stop-color="#0d5674" stop-opacity="0"/>
          <stop offset="0.15" stop-color="#0d5674"/>
          <stop offset="0.9" stop-color="#0d5674"/>
          <stop offset="1" stop-color="#0d5674" stop-opacity="0"/>
        </linearGradient>
      </defs>
      <path d="M20 14 Q363 10 705 14 Q363 17 20 14 Z" fill="url(#swooshGradient)"/>
      <rect x="0" y="18" width="726" height="16" fill="url(#bandGradient)"/>
    </svg>
  </main>
</body>
</html>
```